Powerpoint for consulting dentalpractices on management, improvement, and benchmarks

Fase 1: create 8-15 slides to be used for the model. The are the basic slideexamples for future presentation.
colour scheme and font types as in attachment for older powerpoint. Fonts, logo and colourscheme stay the same. Newer slidedeck contains newer ideas for new presentations. Smaller logo maybe better to be used for all slides. Normal logo for starting and end slide. Open for your inspiration and new suggestions
Fase 2 create slidemaster to enable us to create new slidedesks faster.

Target Market(s)

Dentalpractices (no dental images in powerpoint)

Industry/Entity Type

Dental practices

Font styles to use
Other font styles liked:
• Roobert for heading Normal Text Inter

Requirements
Must have
• Different slidemaster basic slides to quickly create slides with full slide pictures which still have a Molvaro touch. Content slides, slides with bullets and slides to show 3 -5 subjects
Nice to have
• New styling element for recognition of brand
Should not have
• round edges, complex slide master

```html
<!DOCTYPE html>
<html lang="en">
<head>
<meta charset="utf-8">
<title>Molvaro slide deck overview</title>
<link rel="stylesheet" href="https://fonts.googleapis.com/css2?family=Carlito:wght@400;700&family=Inter:wght@400;600;700&display=swap">
<style>
:root{
  --blue:#1266b5;
  --navy:#0b56a3;
  --orange:#f7931e;
  --orange-soft:#f9ad4c;
  --green:#6cbf1b;
  --sky:#a8c6e1;
  --ink:#1d1d1d;
  --muted:#8a8a8a;
  --white:#ffffff;
}
*{margin:0;padding:0;box-sizing:border-box}
html,body{width:1200px;height:1200px;overflow:hidden;background:var(--white)}
body{position:relative;font-family:Inter,Arial,sans-serif;color:var(--ink)}
.slide{position:absolute;width:364px;height:204px;background:var(--white);overflow:hidden;box-shadow:0 3px 9px rgba(0,0,0,.22)}
.abs{position:absolute}
.photo{position:absolute}
.logo{position:absolute;left:30px;top:9px;font-family:Inter,Arial,sans-serif;font-weight:600;font-size:11px;color:var(--blue);letter-spacing:-.2px}
.dots{position:absolute;right:24px;top:11px;display:flex;gap:2px}
.dots i{width:4px;height:4px;border-radius:50%;display:block}
.dots i:nth-child(1){background:var(--blue)}
.dots i:nth-child(2){background:#e0322b}
.dots i:nth-child(3){background:var(--green)}
.footer{position:absolute;left:29px;bottom:4px;font-size:4px;color:var(--muted)}
.pnum{position:absolute;right:24px;bottom:2px;width:15px;height:15px;border:1.3px solid var(--blue);border-radius:50%;font-size:3.6px;color:var(--blue);display:flex;align-items:center;justify-content:center}
.head{font-family:Carlito,Calibri,sans-serif;font-weight:400}
.tiny{font-size:3.7px;line-height:1.65;color:#333}
.tiny.w{color:var(--white)}
.item-num{font-family:Inter,Arial,sans-serif;font-weight:700;font-size:6px;color:var(--blue)}
.item-title{font-weight:700;font-size:5px;color:var(--blue)}
.on-blue .item-num,.on-blue .item-title{color:var(--white)}
.section-title{position:absolute;left:28px;font-family:Carlito,Calibri,sans-serif;font-size:30px;color:var(--white);padding-left:6px;border-left:2px solid var(--white);line-height:1.25}
.ticks{list-style:none}
.ticks li{position:relative;padding-left:5px}
.ticks li::before{content:"\2713";position:absolute;left:0;font-size:3.4px}
.bullets{list-style:none}
.bullets li{position:relative;padding-left:7px}
.bullets li::before{content:"";position:absolute;left:1px;top:2.6px;width:1.6px;height:1.6px;background:currentColor;border-radius:50%}
.tile{position:absolute;top:117px;height:49px;color:var(--white);text-align:center}
.tile b{display:block;font-size:5.3px;margin-top:2px}
.tile p{font-size:3.4px;line-height:1.7;margin-top:3px}
</style>
</head>
<body>

<!-- 1 Title -->
<section class="slide" style="left:37px;top:102px">
  <div class="photo" role="img" aria-label="Shopping cart full of medicine packs with rising bar chart on a pale blue background" style="inset:0;background:linear-gradient(120deg,#b9d3ea 0%,#a6c4df 55%,#c4d8ea 100%)"></div>
  <svg class="abs" style="left:0;top:0" width="364" height="204" viewBox="0 0 364 204"><path d="M0 0H110C170 0 180 60 178 100C176 160 140 204 90 204H0Z" fill="var(--orange)"/></svg>
  <div class="abs" style="left:30px;top:60px;font-weight:600;font-size:28px;color:var(--blue);letter-spacing:-.6px">Molvaro</div>
  <div class="abs head" style="left:8px;top:104px;width:160px;text-align:center;font-size:18.5px;line-height:1.2;color:var(--blue)">Click to edit title Presentation</div>
  <div class="abs" style="left:138px;bottom:6px;font-size:4px;color:var(--white)">Molvaro Confidential – Not for Distribution</div>
  <div class="abs" style="left:331px;bottom:7px;font-size:3.6px;color:#6b7f95">1</div>
</section>

<!-- 2 Overview -->
<section class="slide" style="left:418px;top:102px">
  <div class="abs" style="left:208px;top:0;width:156px;height:128px;background:var(--blue)"></div>
  <div class="logo">Molvaro</div><div class="dots"><i></i><i></i><i></i></div>
  <div class="photo" role="img" aria-label="Doctor holding pills and a yellow ball" style="left:34px;top:36px;width:98px;height:66px;background:linear-gradient(135deg,#eeeeee,#f6e7c9 70%,#e9c43a)"></div>
  <div class="photo" role="img" aria-label="Flat lay of sweets, sugar and glucose meter on blue" style="left:137px;top:36px;width:99px;height:66px;background:linear-gradient(135deg,#6fb6d9,#9ccbe3 50%,#d8b9c5)"></div>
  <div class="photo" role="img" aria-label="Small shopping cart with pills on pale blue" style="left:240px;top:36px;width:98px;height:66px;background:linear-gradient(135deg,#b7d3ea,#a4c4df)"></div>
  <div class="abs head" style="left:37px;top:109px;font-size:11px">Overview</div>
  <div class="abs head" style="left:35px;top:123px;font-size:9px">Lorem Ipsum is simply dummy text</div>
  <ul class="abs tiny ticks" style="left:36px;top:143px;width:96px;text-align:justify"><li>Sample text about practice goals, patient flow and the results we track across each clinic every year.</li></ul>
  <ul class="abs tiny ticks" style="left:151px;top:142px;width:182px;text-align:justify"><li>Sample text on practice management, staffing and monthly review cycles. Short notes on benchmarks and targets for the team. Plain summary of progress and next steps for the year.</li></ul>
  <div class="footer">Molvaro Confidential – Not for Distribution</div><div class="pnum">2</div>
</section>

<!-- 3 Title slide orange -->
<section class="slide" style="left:799px;top:102px">
  <svg class="abs" style="left:0;top:0" width="364" height="204" viewBox="0 0 364 204"><path d="M0 0H364V105C364 116 356 120 346 120H30C12 120 0 132 0 150Z" fill="var(--orange)"/></svg>
  <div class="photo" role="img" aria-label="Faint pattern of pill blister packs" style="left:0;top:0;width:364px;height:60px;background:linear-gradient(180deg,rgba(255,255,255,.12),rgba(255,255,255,0))"></div>
  <div class="logo">Molvaro</div><div class="dots"><i></i><i></i><i></i></div>
  <div class="photo" role="img" aria-label="Doctor holding pills and a yellow ball" style="left:45px;top:47px;width:104px;height:119px;background:linear-gradient(160deg,#f1f1f1,#e9e4da 60%,#e8c33b)"></div>
  <div class="abs head" style="left:167px;top:43px;font-size:17px;color:var(--white)">Click to edit title slide</div>
  <p class="abs tiny w" style="left:168px;top:68px;width:158px;text-align:justify">Sample text about the practice plan and its yearly standard. Notes on benchmarks, team goals and patient care. Brief summary of review cycles and the progress made across each clinic over the year.</p>
  <div class="abs" style="left:168px;top:130px;font-size:5px;font-weight:700">Meaning Of Educating people through sports.</div>
  <p class="abs tiny" style="left:168px;top:140px;width:170px">Sample text on the practice plan and the team goals.<br>Short note on the yearly standard.</p>
  <div class="footer">Molvaro Confidential – Not for Distribution</div><div class="pnum">3</div>
</section>

<!-- 4 Section 1 -->
<section class="slide" style="left:37px;top:366px">
  <div class="logo">Molvaro</div><div class="dots"><i></i><i></i><i></i></div>
  <div class="photo" role="img" aria-label="Hand stopping falling wooden blocks marked risk" style="left:41px;top:32px;width:281px;height:140px;background:linear-gradient(110deg,#c9b59b,#8b9fb4 60%,#6c7f95)"></div>
  <div class="abs" style="left:30px;top:48px;width:281px;height:135px;background:rgba(18,102,181,.82)"></div>
  <div class="section-title" style="top:88px">Section 1</div>
  <div class="footer">Molvaro Confidential – Not for Distribution</div><div class="pnum">4</div>
</section>

<!-- 5 Some Questions -->
<section class="slide" style="left:418px;top:366px">
  <div class="logo">Molvaro</div><div class="dots"><i></i><i></i><i></i></div>
  <div class="abs head" style="left:31px;top:41px;font-size:15px">Some Questions</div>
  <div class="photo" role="img" aria-label="Doctor holding pills and a yellow ball" style="left:26px;top:78px;width:159px;height:87px;background:linear-gradient(135deg,#f2f2f2,#ece6da 55%,#e7c33a)"></div>
  <div class="abs" style="left:167px;top:69px;width:172px;height:39px;background:var(--blue)"></div>
  <div class="abs" style="left:195px;top:42px;width:135px">
    <div><span class="item-num">01.</span> <span class="item-title">Click to edit title slide</span></div>
    <p class="tiny" style="padding-left:14px">Sample text about the plan and the team.<br>Short note on the yearly standard.</p>
  </div>
  <div class="abs on-blue" style="left:195px;top:73px;width:135px">
    <div><span class="item-num">02.</span> <span class="item-title">Click to edit title slide</span></div>
    <p class="tiny w" style="padding-left:14px;margin-top:2px">Sample text about the plan and the team.<br>Short note on the yearly standard.</p>
  </div>
  <div class="abs" style="left:195px;top:114px;width:135px">
    <div><span class="item-num">03.</span> <span class="item-title">Click to edit title slide</span></div>
    <p class="tiny" style="padding-left:14px;margin-top:4px">Sample text about the plan and the team.<br>Short note on the yearly standard.</p>
  </div>
  <div class="abs" style="left:195px;top:147px;width:135px">
    <div><span class="item-num">04.</span> <span class="item-title">Click to edit title slide</span></div>
    <p class="tiny" style="padding-left:14px;margin-top:2px">Sample text about the plan and the team.<br>Short note on the yearly standard.</p>
  </div>
  <div class="footer">Molvaro Confidential – Not for Distribution</div><div class="pnum">5</div>
</section>

<!-- 6 List on photo -->
<section class="slide" style="left:799px;top:366px">
  <div class="logo">Molvaro</div><div class="dots"><i></i><i></i><i></i></div>
  <div class="photo" role="img" aria-label="Laboratory microscope close-up" style="left:0;top:41px;width:174px;height:136px;background:linear-gradient(135deg,#d3e2ee,#8fa7bd 50%,#c8d7e3)"></div>
  <div class="abs head" style="left:185px;top:34px;font-size:15px">Click to edit title slide</div>
  <div class="abs on-blue" style="left:140px;top:57px;width:207px;height:106px;background:var(--blue);padding:7px 0 0 56px">
    <div><span class="item-num">01.</span> <span class="item-title">Click to edit title slide</span></div>
    <p class="tiny w" style="padding-left:14px;margin-bottom:5px">Sample text about the plan and the team.<br>Short note on the yearly standard.</p>
    <div><span class="item-num">02.</span> <span class="item-title">Click to edit title slide</span></div>
    <p class="tiny w" style="padding-left:14px;margin-top:2px;margin-bottom:5px">Sample text about the plan and the team.<br>Short note on the yearly standard.</p>
    <div><span class="item-num">03.</span> <span class="item-title">Click to edit title slide</span></div>
    <p class="tiny w" style="padding-left:14px;margin-top:2px">Sample text about the plan and the team.<br>Short note on the yearly standard.</p>
  </div>
  <div class="footer">Molvaro Confidential – Not for Distribution</div><div class="pnum">6</div>
</section>

<!-- 7 Three subjects -->
<section class="slide" style="left:37px;top:630px">
  <div class="logo">Molvaro</div><div class="dots"><i></i><i></i><i></i></div>
  <div class="abs head" style="left:27px;top:45px;font-size:15px">Click to edit title</div>
  <p class="abs tiny" style="left:27px;top:67px;width:146px;text-align:justify">Sample text about the practice plan and its yearly standard. Notes on benchmarks and team goals for each clinic. Brief summary of the review cycle and patient care. Short line on progress and the next steps for the year ahead.</p>
  <div class="photo" role="img" aria-label="Heap of pink and white pill blister packs" style="left:180px;top:41px;width:152px;height:76px;background:linear-gradient(135deg,#dcdcdc,#e7b9c9 50%,#cfcfcf)"></div>
  <div class="tile" style="left:26px;width:100px;background:var(--navy)">
    <svg width="18" height="16" viewBox="0 0 18 16" style="margin-top:4px"><path d="M2 15H16M4 15V10H7V15M8 15V7H11V15M12 15V4H15V15" stroke="#fff" fill="none" stroke-width="1"/></svg>
    <b>Challenge</b><p>Sample text about the<br>plan and the team</p>
  </div>
  <div class="tile" style="left:131px;width:100px;background:var(--green)">
    <svg width="18" height="16" viewBox="0 0 18 16" style="margin-top:4px"><circle cx="9" cy="8" r="2.5" stroke="#fff" fill="none"/><circle cx="3" cy="3" r="1.6" stroke="#fff" fill="none"/><circle cx="15" cy="3" r="1.6" stroke="#fff" fill="none"/><circle cx="3" cy="13" r="1.6" stroke="#fff" fill="none"/><circle cx="15" cy="13" r="1.6" stroke="#fff" fill="none"/><path d="M4 4L7 6.5M14 4L11 6.5M4 12L7 9.5M14 12L11 9.5" stroke="#fff"/></svg>
    <b>Connectivity</b><p>Sample text about the<br>plan and the team</p>
  </div>
  <div class="tile" style="left:235px;width:100px;background:var(--green)">
    <svg width="20" height="16" viewBox="0 0 20 16" style="margin-top:4px"><circle cx="10" cy="4" r="2.3" stroke="#fff" fill="none"/><circle cx="4" cy="6" r="1.8" stroke="#fff" fill="none"/><circle cx="16" cy="6" r="1.8" stroke="#fff" fill="none"/><path d="M6 15V10H14V15M1 15V11H6M19 15V11H14" stroke="#fff" fill="none"/></svg>
    <b>Creativity</b><p>Sample text about the<br>plan and the team</p>
  </div>
  <div class="footer">Molvaro Confidential – Not for Distribution</div><div class="pnum">7</div>
</section>

<!-- 8 Bullets with photos -->
<section class="slide" style="left:418px;top:630px">
  <div class="logo">Molvaro</div><div class="dots"><i></i><i></i><i></i></div>
  <div class="abs" style="left:0;top:53px;width:182px;height:104px;background:var(--navy);color:var(--white);padding:5px 0 0 32px">
    <div class="head" style="font-size:16px">Click to edit title</div>
    <ul class="bullets" style="font-size:6px;line-height:1.8;margin-top:3px;width:125px">
      <li>Sample text about the plan and the team</li>
      <li>Short notes on benchmarks and yearly goals</li>
      <li>Plain review of care</li>
    </ul>
  </div>
  <div class="photo" role="img" aria-label="Hand stopping falling wooden blocks marked risk" style="left:184px;top:34px;width:87px;height:136px;background:linear-gradient(135deg,#7a8590,#b08e6a 60%,#5b4a3b)"></div>
  <div class="photo" role="img" aria-label="Doctor holding pills and a yellow ball" style="left:275px;top:34px;width:89px;height:136px;background:linear-gradient(160deg,#f3f3f3,#ebe4d6 60%,#e6c23b)"></div>
  <div class="footer">Molvaro Confidential – Not for Distribution</div><div class="pnum">8</div>
</section>

<!-- 9 Reflective Questions -->
<section class="slide" style="left:799px;top:630px">
  <div class="logo">Molvaro</div><div class="dots"><i></i><i></i><i></i></div>
  <div class="abs" style="left:0;top:37px;width:364px;height:144px;background:var(--navy)"></div>
  <div class="photo" role="img" aria-label="Doctor holding pills and a yellow ball" style="left:25px;top:43px;width:165px;height:131px;background:linear-gradient(150deg,#f4f4f4,#ece5d7 60%,#e6c23a)"></div>
  <div class="abs head" style="left:209px;top:43px;font-size:11.5px;color:var(--white)">Reflective Questions</div>
  <ul class="abs bullets" style="left:213px;top:64px;width:136px;font-size:4.5px;line-height:1.45;color:var(--white)">
    <li style="margin-bottom:5px">Sample text on the practice plan and team goals for each clinic this year.</li>
    <li style="margin-bottom:5px">Sample text on the practice plan and team goals. Short notes on benchmarks and the yearly review of patient care.</li>
    <li style="margin-bottom:5px">Sample text on the practice plan and team goals for each clinic this year.</li>
    <li>Short note on progress made. Sample text on the plan and team goals.</li>
  </ul>
  <div class="footer">Molvaro Confidential – Not for Distribution</div><div class="pnum">9</div>
</section>

<!-- 10 Section 2 -->
<section class="slide" style="left:37px;top:894px">
  <div class="logo">Molvaro</div><div class="dots"><i></i><i></i><i></i></div>
  <div class="abs" style="left:41px;top:32px;width:281px;height:140px;background:var(--sky)"></div>
  <div class="photo" role="img" aria-label="Shopping cart full of medicine packs, orange toned" style="left:30px;top:48px;width:281px;height:135px;background:linear-gradient(135deg,#f2a441,#f6ae52 50%,#efa540)"></div>
  <div class="section-title" style="top:88px">Section 2</div>
  <div class="footer">Molvaro Confidential – Not for Distribution</div><div class="pnum">10</div>
</section>

<!-- 11 Overview orange -->
<section class="slide" style="left:418px;top:894px">
  <div class="abs" style="left:208px;top:0;width:156px;height:128px;background:var(--orange)"></div>
  <div class="logo">Molvaro</div><div class="dots"><i></i><i></i><i></i></div>
  <div class="photo" role="img" aria-label="Hand stopping falling wooden blocks marked risk" style="left:25px;top:36px;width:98px;height:66px;background:linear-gradient(135deg,#6f7f8f,#b08e6a 60%,#5d4c3c)"></div>
  <div class="photo" role="img" aria-label="Heap of pink and white pill blister packs" style="left:145px;top:36px;width:98px;height:66px;background:linear-gradient(135deg,#d9d9d9,#e5b3c4 50%,#e8a35a)"></div>
  <p class="abs" style="left:262px;top:40px;width:76px;font-size:5.2px;line-height:1.9;color:var(--white);text-align:justify">Sample text about the practice plan and team goals. Short notes on each clinic and its yearly benchmark review and care.</p>
  <div class="abs head" style="left:29px;top:109px;font-size:15px">Overview</div>
  <p class="abs" style="left:29px;top:136px;width:100px;font-size:5px;line-height:1.9">Sample text about the practice plan and team goals for each clinic and its review.</p>
  <ul class="abs tiny ticks" style="left:140px;top:134px;width:196px">
    <li style="margin-bottom:6px">Sample text on practice management and the team. Short notes on benchmarks and monthly review cycles across clinics.</li>
    <li>Sample text on practice management and the team. Short notes on benchmarks and monthly review cycles across clinics.</li>
  </ul>
  <div class="footer">Molvaro Confidential – Not for Distribution</div><div class="pnum">11</div>
</section>

<!-- 12 Objectives -->
<section class="slide" style="left:799px;top:894px">
  <div class="logo">Molvaro</div><div class="dots"><i></i><i></i><i></i></div>
  <div class="photo" role="img" aria-label="Laboratory microscope close-up" style="left:0;top:42px;width:132px;height:162px;background:linear-gradient(135deg,#cddbe8,#8aa3ba 50%,#b8c9d8)"></div>
  <div class="abs head" style="left:158px;top:42px;font-size:15px;line-height:1.3">Objectives Of Financial<br><span style="color:var(--blue)">Management Here</span></div>
  <div class="abs" style="left:75px;top:88px;width:72px;height:72px;background:var(--navy);text-align:center;color:var(--white)">
    <svg width="34" height="34" viewBox="0 0 34 34" style="margin-top:8px"><circle cx="17" cy="17" r="13" fill="none" stroke="var(--green)" stroke-width="2.4" stroke-dasharray="70 12"/><text x="17" y="19" text-anchor="middle" font-size="5.5" fill="#fff" font-family="Inter,Arial,sans-serif">+351</text></svg>
    <div style="font-size:4.2px;font-weight:700;color:var(--green)">First Detail</div>
    <p style="font-size:3.4px;line-height:1.7;color:#9bc3e8">Sample text about<br>the plan and the team</p>
  </div>
  <div class="abs" style="left:152px;top:94px;width:72px;height:76px;background:var(--white);box-shadow:0 1px 4px rgba(0,0,0,.18);text-align:center">
    <svg width="34" height="34" viewBox="0 0 34 34" style="margin-top:7px"><circle cx="17" cy="17" r="13" fill="none" stroke="var(--navy)" stroke-width="2.4" stroke-dasharray="70 12"/><text x="17" y="19" text-anchor="middle" font-size="5.5" fill="var(--navy)" font-weight="700" font-family="Inter,Arial,sans-serif">40%</text></svg>
    <div style="font-size:4.2px;font-weight:700;color:var(--navy)">Second Detail</div>
    <p style="font-size:3.4px;line-height:1.7;color:var(--blue)">Sample text about<br>the plan and the team</p>
  </div>
  <div class="abs" style="left:240px;top:96px;width:82px">
    <div class="item-title" style="font-size:5.3px">Financial Plan.</div>
    <p class="tiny" style="margin:2px 0 7px">Sample text on the yearly plan and the team goals for each clinic.</p>
    <div class="item-title" style="font-size:5.3px">Financial Target.</div>
    <p class="tiny" style="margin-top:2px">Sample text on the yearly plan and the team goals.</p>
  </div>
  <div class="abs" style="left:29px;bottom:4px;font-size:4px;color:var(--white)">Molvaro Confidential – Not for Distribution</div><div class="pnum">12</div>
</section>

</body>
</html>
```